Web-Based Software Platform - 34 Individual designs for user interface

We have a new piece of software that requires 34 individual "tiles" for a user interface. An example of the way they will be displayed is included in the file, along with examples of 34 tiles that we created in house.

There is a title associated with each tile. This is all real estate related.

image sizes needed

width: 290px
height: 218px

Target Market(s)

real estate users

Industry/Entity Type

Real Estate

Number of Pages Required

1 page

Font styles to use
Sans Serif

Colors
3176b5
fbee3d
9bcb3b
f37122

Requirements
Must have
• 34 seperate images
Nice to have
• see file
Should not have
• see file

```html
<!DOCTYPE html>
<html lang="en">
<head>
<meta charset="utf-8">
<title>List Tiles</title>
<link href="https://fonts.googleapis.com/css2?family=Playfair+Display:wght@800&family=Montserrat:wght@600;700&display=swap" rel="stylesheet">
<style>
  :root {
    --page-bg: #ffffff;
    --ink: #1c1c1c;
    --label-ink: #2e2e2e;
    --cash-red: #b01c1f;
    --cash-red-deep: #8e1215;
    --lender-green: #25852a;
    --lender-green-deep: #17631b;
    --campaign-plum: #93205f;
    --campaign-plum-deep: #6f1448;
    --badge-white: #ffffff;
    --icon-blue: #3176b5;
    --icon-red: #d23a3a;
    --icon-green: #4f9a34;
  }
  * { margin: 0; padding: 0; box-sizing: border-box; }
  html, body { width: 1200px; height: 2800px; overflow: hidden; background: var(--page-bg); }
  .canvas { position: relative; width: 1200px; height: 2800px; }

  .section-title {
    position: absolute; left: 0; width: 1200px; text-align: center;
    font-family: "Playfair Display", Georgia, serif; font-weight: 800;
    font-size: 42px; letter-spacing: 2px; text-transform: uppercase; color: var(--ink);
  }
  .tile-grid {
    position: absolute; left: 100px;
    display: grid; grid-template-columns: repeat(3, 312px);
    column-gap: 32px; grid-auto-rows: 308px;
  }
  .tile-item { display: flex; flex-direction: column; align-items: center; }
  .tile {
    position: relative; width: 312px; height: 204px;
    display: flex; align-items: center; justify-content: center;
  }
  .tile--cash { background: radial-gradient(circle at 50% 50%, var(--cash-red) 0%, var(--cash-red-deep) 100%); }
  .tile--lender { background: radial-gradient(circle at 50% 50%, var(--lender-green) 0%, var(--lender-green-deep) 100%); }
  .tile--campaign { background: radial-gradient(circle at 50% 50%, var(--campaign-plum) 0%, var(--campaign-plum-deep) 100%); }
  .tile-pattern { position: absolute; inset: 0; }

  .badge {
    position: relative;
    width: 100px; height: 100px; border-radius: 50%;
    background: var(--badge-white);
    display: flex; align-items: center; justify-content: center;
    box-shadow: 0 0 0 5px rgba(255,255,255,0.3);
  }
  .badge-icon { width: 56px; height: 56px; }
  .ico { fill: none; stroke-width: 2.6; stroke-linecap: round; stroke-linejoin: round; }
  .ico-main { stroke: var(--icon-blue); }
  .ico-accent { stroke: var(--icon-red); }
  .tile--lender .ico-accent { stroke: var(--icon-green); }
  .ico-glyph { font-family: "Montserrat", Arial, sans-serif; font-weight: 700; font-size: 13px; fill: var(--icon-red); stroke: none; }
  .tile--lender .ico-glyph { fill: var(--icon-green); }

  .tile-label {
    margin-top: 22px; width: 270px; text-align: center;
    font-family: "Montserrat", Arial, sans-serif; font-weight: 600;
    font-size: 13px; line-height: 1.55; letter-spacing: 0.4px;
    text-transform: uppercase; color: var(--label-ink);
  }
</style>
</head>
<body>
<svg width="0" height="0" style="position:absolute" aria-hidden="true">
  <defs>
    <symbol id="i-users" viewBox="0 0 48 48"><g class="ico ico-main"><circle cx="17" cy="17" r="5"/><circle cx="31" cy="17" r="5"/><path d="M8 36c0-6 4-10 9-10s9 4 9 10"/><path d="M22 36c0-6 4-10 9-10s9 4 9 10"/></g></symbol>
    <symbol id="i-house-cash" viewBox="0 0 48 48"><g class="ico ico-main"><path d="M8 24L24 10l16 14"/><path d="M12 21v17h24V21"/></g><circle class="ico ico-accent" cx="24" cy="29" r="6"/><text class="ico-glyph" x="24" y="33.5" text-anchor="middle">$</text></symbol>
    <symbol id="i-user-tool" viewBox="0 0 48 48"><g class="ico ico-main"><circle cx="22" cy="16" r="7"/><path d="M9 40c0-8 6-13 13-13"/></g><g class="ico ico-accent"><circle cx="34" cy="34" r="6"/><path d="M38 38l4 4"/></g></symbol>
    <symbol id="i-user-pin" viewBox="0 0 48 48"><g class="ico ico-main"><circle cx="19" cy="16" r="6"/><path d="M7 38c0-7 5-12 12-12"/></g><g class="ico ico-accent"><path d="M34 42s-8-8-8-14a8 8 0 0116 0c0 6-8 14-8 14z"/><circle cx="34" cy="28" r="2.5"/></g></symbol>
    <symbol id="i-building" viewBox="0 0 48 48"><g class="ico ico-main"><rect x="12" y="8" width="24" height="32"/><path d="M18 15h4M26 15h4M18 22h4M26 22h4M18 29h4M26 29h4"/></g><path class="ico ico-accent" d="M21 40v-5h6v5"/></symbol>
    <symbol id="i-boxes" viewBox="0 0 48 48"><g class="ico ico-main"><rect x="8" y="24" width="14" height="14"/><rect x="26" y="24" width="14" height="14"/></g><rect class="ico ico-accent" x="17" y="9" width="14" height="14"/></symbol>
    <symbol id="i-lender" viewBox="0 0 48 48"><g class="ico ico-main"><circle cx="18" cy="15" r="6"/><path d="M7 38c0-8 5-13 11-13s11 5 11 13"/></g><circle class="ico ico-accent" cx="35" cy="22" r="7"/><text class="ico-glyph" x="35" y="26.5" text-anchor="middle">$</text></symbol>
    <symbol id="i-coin-up" viewBox="0 0 48 48"><rect class="ico ico-main" x="9" y="10" width="30" height="28" rx="3"/><circle class="ico ico-accent" cx="22" cy="24" r="8"/><text class="ico-glyph" x="22" y="28.5" text-anchor="middle">$</text><path class="ico ico-main" d="M34 28V17m-3 3l3-3 3 3"/></symbol>
    <symbol id="i-coin-down" viewBox="0 0 48 48"><rect class="ico ico-main" x="9" y="10" width="30" height="28" rx="3"/><circle class="ico ico-accent" cx="22" cy="24" r="8"/><text class="ico-glyph" x="22" y="28.5" text-anchor="middle">$</text><path class="ico ico-main" d="M34 17v11m-3-3l3 3 3-3"/></symbol>
    <symbol id="i-hand-lender" viewBox="0 0 48 48"><circle class="ico ico-accent" cx="24" cy="16" r="7"/><text class="ico-glyph" x="24" y="20.5" text-anchor="middle">$</text><path class="ico ico-main" d="M8 32h8l6 3h8l8-5M8 40h26l8-6"/></symbol>
    <symbol id="i-pin" viewBox="0 0 48 48"><g class="ico ico-main"><path d="M24 42s-11-11-11-19a11 11 0 0122 0c0 8-11 19-11 19z"/></g><circle class="ico ico-accent" cx="24" cy="23" r="4"/></symbol>
    <symbol id="i-card" viewBox="0 0 48 48"><rect class="ico ico-main" x="7" y="12" width="34" height="24" rx="3"/><circle class="ico ico-accent" cx="17" cy="22" r="4"/><path class="ico ico-main" d="M26 19h10M26 25h10M12 31h24"/></symbol>
    <symbol id="i-envelopes" viewBox="0 0 48 48"><g class="ico ico-main"><rect x="10" y="16" width="30" height="20" rx="2"/><path d="M10 17l15 11 15-11"/></g><path class="ico ico-accent" d="M6 12h26"/></symbol>
    <symbol id="i-envelope" viewBox="0 0 48 48"><g class="ico ico-main"><rect x="8" y="14" width="32" height="22" rx="2"/><path d="M8 15l16 12 16-12"/></g><circle class="ico ico-accent" cx="38" cy="13" r="4"/></symbol>
    <symbol id="i-screen-phone" viewBox="0 0 48 48"><g class="ico ico-main"><rect x="6" y="10" width="36" height="24" rx="2"/><path d="M18 40h12M24 34v6"/></g><path class="ico ico-accent" d="M19 17c0 6 4 10 10 10l2-3-3-2-2 1c-2-1-3-2-4-4l1-2-2-3z"/></symbol>
    <symbol id="i-screen-mail" viewBox="0 0 48 48"><g class="ico ico-main"><rect x="6" y="10" width="36" height="24" rx="2"/><path d="M18 40h12M24 34v6"/></g><g class="ico ico-accent"><rect x="16" y="16" width="16" height="12"/><path d="M16 17l8 6 8-6"/></g></symbol>
    <symbol id="i-document" viewBox="0 0 48 48"><g class="ico ico-main"><path d="M12 6h17l8 8v28H12z"/><path d="M29 6v8h8"/><path d="M17 22h14M17 28h14M17 34h9"/></g><circle class="ico ico-accent" cx="36" cy="38" r="5"/></symbol>
    <symbol id="i-mail-edit" viewBox="0 0 48 48"><g class="ico ico-main"><rect x="6" y="16" width="28" height="20" rx="2"/><path d="M6 17l14 10 14-10"/></g><path class="ico ico-accent" d="M30 36l12-12-4-4-12 12-1 5z"/></symbol>
  </defs>
</svg>

<main class="canvas">

  <h2 class="section-title" style="top:92px">Cash Buyer Lists</h2>
  <section class="tile-grid" style="top:228px">
    <div class="tile-item"><div class="tile tile--cash"><div class="tile-pattern" role="img" aria-label="Faint real estate line pattern"></div><div class="badge"><svg class="badge-icon" role="img" aria-label="Group of buyers"><use href="#i-users"/></svg></div></div><p class="tile-label">Multi Deal Cash Buyers</p></div>
    <div class="tile-item"><div class="tile tile--cash"><div class="tile-pattern" role="img" aria-label="Faint real estate line pattern"></div><div class="badge"><svg class="badge-icon" role="img" aria-label="House with cash"><use href="#i-house-cash"/></svg></div></div><p class="tile-label">Active Cash Buyers</p></div>
    <div class="tile-item"><div class="tile tile--cash"><div class="tile-pattern" role="img" aria-label="Faint real estate line pattern"></div><div class="badge"><svg class="badge-icon" role="img" aria-label="Buyer with tool"><use href="#i-user-tool"/></svg></div></div><p class="tile-label">Fix N Flip Buyers</p></div>
    <div class="tile-item"><div class="tile tile--cash"><div class="tile-pattern" role="img" aria-label="Faint real estate line pattern"></div><div class="badge"><svg class="badge-icon" role="img" aria-label="Buyer with location pin"><use href="#i-user-pin"/></svg></div></div><p class="tile-label">Out-of-State Cash Buyers</p></div>
    <div class="tile-item"><div class="tile tile--cash"><div class="tile-pattern" role="img" aria-label="Faint real estate line pattern"></div><div class="badge"><svg class="badge-icon" role="img" aria-label="Commercial building"><use href="#i-building"/></svg></div></div><p class="tile-label">Commercial Cash Buyers</p></div>
    <div class="tile-item"><div class="tile tile--cash"><div class="tile-pattern" role="img" aria-label="Faint real estate line pattern"></div><div class="badge"><svg class="badge-icon" role="img" aria-label="Stacked boxes"><use href="#i-boxes"/></svg></div></div><p class="tile-label">Wholesale Buyers</p></div>
  </section>

  <h2 class="section-title" style="top:872px">Private Lender Lists</h2>
  <section class="tile-grid" style="top:1008px">
    <div class="tile-item"><div class="tile tile--lender"><div class="tile-pattern" role="img" aria-label="Faint real estate line pattern"></div><div class="badge"><svg class="badge-icon" role="img" aria-label="Lender with coin"><use href="#i-lender"/></svg></div></div><p class="tile-label">Active Private Lenders</p></div>
    <div class="tile-item"><div class="tile tile--lender"><div class="tile-pattern" role="img" aria-label="Faint real estate line pattern"></div><div class="badge"><svg class="badge-icon" role="img" aria-label="Coin with up arrow"><use href="#i-coin-up"/></svg></div></div><p class="tile-label">Private Lenders - Above $500K</p></div>
    <div class="tile-item"><div class="tile tile--lender"><div class="tile-pattern" role="img" aria-label="Faint real estate line pattern"></div><div class="badge"><svg class="badge-icon" role="img" aria-label="Coin with down arrow"><use href="#i-coin-down"/></svg></div></div><p class="tile-label">Private Lenders - Under $500K</p></div>
    <div class="tile-item"><div class="tile tile--lender"><div class="tile-pattern" role="img" aria-label="Faint real estate line pattern"></div><div class="badge"><svg class="badge-icon" role="img" aria-label="Hand holding coin"><use href="#i-hand-lender"/></svg></div></div><p class="tile-label">Out-of-State Private Lenders</p></div>
  </section>

  <h2 class="section-title" style="top:1676px">Campaign Lists</h2>
  <section class="tile-grid" style="top:1820px">
    <div class="tile-item"><div class="tile tile--campaign"><div class="tile-pattern" role="img" aria-label="Faint real estate line pattern"></div><div class="badge"><svg class="badge-icon" role="img" aria-label="Location pin"><use href="#i-pin"/></svg></div></div><p class="tile-label">Data Export - Address Only</p></div>
    <div class="tile-item"><div class="tile tile--campaign"><div class="tile-pattern" role="img" aria-label="Faint real estate line pattern"></div><div class="badge"><svg class="badge-icon" role="img" aria-label="Contact card"><use href="#i-card"/></svg></div></div><p class="tile-label">Data Export - Append Phone, Email</p></div>
    <div class="tile-item"><div class="tile tile--campaign"><div class="tile-pattern" role="img" aria-label="Faint real estate line pattern"></div><div class="badge"><svg class="badge-icon" role="img" aria-label="Envelope in motion"><use href="#i-envelopes"/></svg></div></div><p class="tile-label">Direct Mail - 5 Touch Campaign</p></div>
    <div class="tile-item"><div class="tile tile--campaign"><div class="tile-pattern" role="img" aria-label="Faint real estate line pattern"></div><div class="badge"><svg class="badge-icon" role="img" aria-label="Envelope"><use href="#i-envelope"/></svg></div></div><p class="tile-label">Direct Mail - 1 Touch Campaign</p></div>
    <div class="tile-item"><div class="tile tile--campaign"><div class="tile-pattern" role="img" aria-label="Faint real estate line pattern"></div><div class="badge"><svg class="badge-icon" role="img" aria-label="Screen with phone"><use href="#i-screen-phone"/></svg></div></div><p class="tile-label">Data Export - Append Phone</p></div>
    <div class="tile-item"><div class="tile tile--campaign"><div class="tile-pattern" role="img" aria-label="Faint real estate line pattern"></div><div class="badge"><svg class="badge-icon" role="img" aria-label="Screen with email"><use href="#i-screen-mail"/></svg></div></div><p class="tile-label">Data Export - Append Email</p></div>
    <div class="tile-item"><div class="tile tile--campaign"><div class="tile-pattern" role="img" aria-label="Faint real estate line pattern"></div><div class="badge"><svg class="badge-icon" role="img" aria-label="Data document"><use href="#i-document"/></svg></div></div><p class="tile-label">1 Touch Campaign - With All Data Appends</p></div>
    <div class="tile-item"><div class="tile tile--campaign"><div class="tile-pattern" role="img" aria-label="Faint real estate line pattern"></div><div class="badge"><svg class="badge-icon" role="img" aria-label="Envelope with pencil"><use href="#i-mail-edit"/></svg></div></div><p class="tile-label">Custom Build Your Direct Mail Campaign</p></div>
  </section>

</main>
</body>
</html>
```